Visitenkarten für eine Hypnose-Praxis
Ich bin sehr zufrieden mit der professionellen Arbeitsweise von KOR7342. Es war immer ein netter Kontakt und meine Wünsche wurden schnell umgesetzt. Alle Vorschläge waren sehr kreativ und und so viel es mir leicht, eine schnelle Entscheidung zu treffen.
Zielgruppe
Wir sind eine Hypnose-Praxis und richten unser Angebot an Privatpersonen unterschiedlichen Alters, die therapeutische Unterstützung suchen.
Aufgabenstellung
Eher schlichtes und modernes Design

```html
<!DOCTYPE html>
<html lang="de">
<head>
<meta charset="utf-8">
<title>Ruhewelle – Visitenkarten</title>
<link rel="stylesheet" href="https://fonts.googleapis.com/css2?family=Lato:ital,wght@0,400;0,700;1,700&display=swap">
<style>
  :root {
    --bg: #f5f5f5;
    --card: #ffffff;
    --ink: #1a1a1a;
    --band-top: #7cc7c9;
    --band-bottom: #8db8d6;
    --link: #3a9fcf;
  }
  * { box-sizing: border-box; margin: 0; padding: 0; }
  html, body { width: 1200px; height: 848px; overflow: hidden; }
  body { background: var(--bg); font-family: "Lato", sans-serif; color: var(--ink); position: relative; }

  .card {
    position: absolute;
    top: 333px;
    width: 396px;
    height: 233px;
    background: var(--card);
    overflow: hidden;
  }
  .card--front { left: 132px; }
  .card--back { left: 609px; }

  .card__band {
    position: absolute;
    top: 0;
    right: 0;
    width: 100px;
    height: 100%;
  }

  .brand {
    position: absolute;
    left: 32px;
    top: 126px;
  }
  .brand__name { font-size: 38px; font-weight: 700; color: var(--ink); line-height: 1; }

  .contact {
    position: absolute;
    left: 72px;
    top: 44px;
    font-size: 10.5px;
    line-height: 14px;
  }
  .contact__name { font-size: 14.5px; font-weight: 700; font-style: italic; line-height: 18px; }
  .contact__group { margin-bottom: 5px; }
  .contact__row { display: flex; white-space: nowrap; }
  .contact__label { width: 62px; }
  .contact__link { color: var(--link); }
</style>
</head>
<body>
  <section class="card card--front">
    <svg class="card__band" viewBox="0 0 100 233" preserveAspectRatio="none" aria-hidden="true">
      <defs>
        <linearGradient id="bandFront" x1="0" y1="0" x2="0" y2="1">
          <stop offset="0" stop-color="#7cc7c9"/>
          <stop offset="1" stop-color="#8db8d6"/>
        </linearGradient>
      </defs>
      <path fill="url(#bandFront)" d="M60 0 H100 V233 H20 Z"/>
    </svg>
    <div class="brand">
      <span class="brand__name">Ruhewelle</span>
    </div>
  </section>

  <section class="card card--back">
    <svg class="card__band" viewBox="0 0 100 233" preserveAspectRatio="none" aria-hidden="true">
      <defs>
        <linearGradient id="bandBack" x1="0" y1="0" x2="0" y2="1">
          <stop offset="0" stop-color="#7cc7c9"/>
          <stop offset="1" stop-color="#8db8d6"/>
        </linearGradient>
      </defs>
      <path fill="url(#bandBack)" d="M60 0 H100 V233 H20 Z"/>
    </svg>
    <div class="contact">
      <p class="contact__name">Lena Morwitz</p>
      <div class="contact__group">
        <p>Diplom-Psychologin</p>
        <p>Heilpraktikerin für Psychotherapie</p>
        <p>mit Spezialisierung Hypnose-Therapie</p>
      </div>
      <div class="contact__group">
        <p>Lindenweg 14</p>
        <p>10115 Berlin</p>
      </div>
      <div class="contact__group">
        <p class="contact__row"><span class="contact__label">Telefon</span>030 / 55 21 40 87</p>
        <p class="contact__row"><span class="contact__label">24-Std-AB</span>030 / 55 21 40 88</p>
      </div>
      <p class="contact__link">info@ruhewelle-praxis.de</p>
      <p class="contact__link">www.ruhewelle-praxis.de</p>
    </div>
  </section>
</body>
</html>
```